Harbourline Electrical limited business card design

I need a business card made up it must be double sided with just my logo and some graphic one side and then on the reverse a little description of services I provide along with my email address phone number and face book and instagram handles
I already had a logo designed by pixel meadow and the social media pack so I’m thinking to use the social media design as the main image
Services I provide are: domestic commercial industrial sub contract from bathroom's and kitchen’s to outside lights and sockets no job to big or to small

Industry/Entity Type

Electrician/construction industry

Contact Information for Business Card

Email address: harbourlineelectrical@mailvane.com mobile number: 07855402917 fb: Harbourline Electrical insta: @harbourlineelectrical

Font styles to use
Sans Serif

Colors
0094D4
00A9DD
6FCCEA
C7EBF8
E9F6FB
FFF300
FFF600
FEFA6F
FFFEC7
FFFEE8

Requirements
Must have
• Double sided, fb and insta handles contact info, domestic commercial industrial sub contract
Nice to have
• From bathroom's and kitchen’s to outside outside lights and sockets no job to big or to small

```html
<!DOCTYPE html>
<html lang="en">
<head>
<meta charset="utf-8">
<title>Harbourline Electrical – Business Card</title>
<link rel="stylesheet" href="https://fonts.googleapis.com/css2?family=Montserrat:wght@400;500;800&display=swap">
<style>
  :root {
    --backdrop: #4a4a4a;
    --card: #171717;
    --brand-blue: #0a8ccb;
    --brand-yellow: #f6c443;
    --text-light: #f2f2f2;
    --text-muted: #bdbdbd;
  }
  * { box-sizing: border-box; margin: 0; padding: 0; }
  html, body { width: 1200px; height: 801px; overflow: hidden; }
  body {
    background: var(--backdrop);
    font-family: "Montserrat", sans-serif;
    display: flex;
    align-items: center;
    justify-content: center;
    gap: 40px;
  }
  .card {
    position: relative;
    width: 540px;
    height: 309px;
    background: var(--card);
    border-radius: 18px;
    border-bottom: 4px solid var(--brand-blue);
    border-left: 2px solid var(--brand-blue);
    box-shadow: 0 18px 30px rgba(0,0,0,0.35);
  }

  /* Contact side */
  .card-contact .brand {
    position: absolute;
    top: 30px;
    right: 30px;
    display: flex;
    align-items: center;
    gap: 10px;
  }
  .brand-dot {
    width: 34px;
    height: 34px;
    border-radius: 50%;
    border: 3px solid var(--brand-blue);
  }
  .brand-name {
    color: var(--brand-blue);
    font-weight: 800;
    font-size: 17px;
    line-height: 1.1;
    text-transform: uppercase;
    letter-spacing: 0.5px;
  }
  .services {
    position: absolute;
    top: 34px;
    left: 34px;
    width: 270px;
  }
  .services-list {
    color: var(--brand-yellow);
    font-weight: 500;
    font-size: 11px;
    text-transform: uppercase;
    letter-spacing: 0.6px;
    line-height: 1.5;
  }
  .services-note {
    color: var(--text-muted);
    font-size: 11px;
    line-height: 1.5;
    margin-top: 6px;
  }
  .socials {
    position: absolute;
    top: 108px;
    right: 30px;
    list-style: none;
  }
  .socials li {
    display: flex;
    align-items: center;
    gap: 9px;
    color: var(--text-light);
    font-size: 13px;
    margin-bottom: 9px;
  }
  .social-dot {
    width: 15px;
    height: 15px;
    border-radius: 50%;
    background: var(--brand-blue);
  }
  .person {
    position: absolute;
    left: 34px;
    bottom: 34px;
  }
  .person-name {
    font-weight: 800;
    font-size: 22px;
    text-transform: uppercase;
    letter-spacing: 0.5px;
  }
  .person-name .first { color: var(--brand-yellow); }
  .person-name .last { color: var(--brand-blue); }
  .person-role {
    color: var(--text-light);
    font-size: 14px;
    margin-top: 2px;
    margin-bottom: 22px;
  }
  .contact-list { list-style: none; }
  .contact-list li {
    display: flex;
    align-items: center;
    gap: 10px;
    color: var(--text-light);
    font-size: 14px;
    margin-top: 7px;
  }
  .contact-list svg { width: 14px; height: 14px; flex: none; }

  /* Logo side */
  .card-logo {
    display: flex;
    flex-direction: column;
    align-items: center;
    justify-content: center;
    gap: 14px;
  }
  .card-logo .brand-dot {
    width: 90px;
    height: 90px;
    border-width: 5px;
  }
  .card-logo .brand-name {
    font-size: 36px;
    text-align: center;
    letter-spacing: 1px;
  }
</style>
</head>
<body>

  <section class="card card-contact" aria-label="Business card, contact side">
    <div class="services">
      <p class="services-list">Domestic · Commercial<br>Industrial · Sub Contract</p>
      <p class="services-note">Bathrooms, kitchens, outside lights and sockets.<br>No job too big or too small.</p>
    </div>

    <div class="brand">
      <span class="brand-dot"></span>
      <span class="brand-name">Harbourline<br>Electrical</span>
    </div>

    <ul class="socials">
      <li><span class="social-dot"></span>Harbourline Electrical</li>
      <li><span class="social-dot"></span>@harbourlineelectrical</li>
    </ul>

    <div class="person">
      <h1 class="person-name"><span class="first">Daniel</span> <span class="last">Harlow</span></h1>
      <p class="person-role">Managing Director</p>
      <ul class="contact-list">
        <li>
          <svg viewBox="0 0 14 14" aria-hidden="true"><rect x="3" y="1" width="8" height="12" rx="1.5" fill="none" stroke="#0a8ccb" stroke-width="1.5"/><line x1="6" y1="11" x2="8" y2="11" stroke="#0a8ccb" stroke-width="1.2"/></svg>
          07855402917
        </li>
        <li>
          <svg viewBox="0 0 14 14" aria-hidden="true"><rect x="1" y="3" width="12" height="8" rx="1" fill="#0a8ccb"/><polyline points="1,3.5 7,8 13,3.5" fill="none" stroke="#171717" stroke-width="1.2"/></svg>
          harbourlineelectrical@mailvane.com
        </li>
      </ul>
    </div>
  </section>

  <section class="card card-logo" aria-label="Business card, logo side">
    <span class="brand-dot"></span>
    <span class="brand-name">Harbourline<br>Electrical</span>
  </section>

</body>
</html>
```